Financial Services Company Needs New UI/UX

Hello!

We would like to see some UI/UX ideas for our software platform. I've attached a screen capture of our current "dashboard" (or main home page, essentially). We're looking for a very simple, clean, sleek design as there are many different pages throughout the system that will all need to coordinate. You can also view our website to see the colors and general "look" we have on there. It would be ideal for the portal to coordinate with the website since that is how they access the login page. Please submit your best ideas for the dashboard and we will reach out to our favorite designer to move forward with the rest of the pages. You can find our color hex codes on our website on the "Media" page. Should you need any other supporting logos or files please send us a message and we will try to accommodate.

Thanks!

Website: www.ledgerharbor-example.com

Target Market(s)

Our clients are contractors in the construction industry and our software helps them manage material purchases for their jobs.

Industry/Entity Type

Financial Service

Font styles to use
Sans Serif

Requirements
Must have
• The same content and language as the current dashboard but an updated look.
Should not have
• Too much distraction or busy patterns, we're looking for clean and simple and user friendly. Likely a solid or subtly textured background would be best.

```html
<!DOCTYPE html>
<html lang="en">
<head>
<meta charset="utf-8">
<title>LedgerHarbor — Dashboard</title>
<link rel="stylesheet" href="https://fonts.googleapis.com/css2?family=Open+Sans:wght@400;600;700&display=swap">
<style>
  :root{
    --page:#dfe5ec;
    --ink:#2b2b2b;
    --muted:#6a6a6a;
    --black:#000;
    --logo-bg:#1f2328;
    --side:#4a8ad4;
    --btn:#3f7fc6;
    --content:#f3f3f3;
    --card:#f6f6f6;
    --line:#e2e2e2;
    --green:#2bb24c;
    --amber:#d9a520;
    --red:#d0342c;
  }
  *{box-sizing:border-box;margin:0;padding:0}
  html,body{width:1200px;height:857px;overflow:hidden}
  body{background:var(--page);font-family:"Open Sans",Arial,sans-serif;color:var(--ink)}
  .app{position:absolute;left:99px;top:99px;width:1003px;height:658px;background:var(--content);box-shadow:0 6px 24px rgba(0,0,0,.12);overflow:hidden}
  .topbar{position:absolute;left:0;top:0;width:100%;height:60px;background:var(--black);color:#fff}
  .brand{position:absolute;left:0;top:0;width:171px;height:60px;background:var(--logo-bg);display:flex;align-items:center;gap:8px;padding-left:18px;font-size:15px;font-weight:400;color:#fff}
  .brand-dot{width:22px;height:22px;border-radius:50%;background:var(--side)}
  .nav{position:absolute;left:212px;top:0;height:60px;display:flex;align-items:center;font-size:11px}
  .nav-item{display:flex;align-items:center;gap:6px;padding:0 19px;border-left:1px solid #555;line-height:13px}
  .nav-item:first-child{border-left:none;padding-left:0}
  .nav-item svg{width:11px;height:11px;fill:#fff}
  .tools{position:absolute;right:22px;top:0;height:60px;display:flex;align-items:center;gap:27px}
  .tools svg{width:16px;height:16px;fill:none;stroke:#fff;stroke-width:2}
  .sidebar{position:absolute;left:0;top:60px;width:60px;height:598px;background:var(--side)}
  .side-icon{position:absolute;left:22px;width:16px;height:16px;fill:none;stroke:#bfe0ff;stroke-width:1.8}
  .side-pointer{position:absolute;left:54px;top:26px;width:0;height:0;border-top:7px solid transparent;border-bottom:7px solid transparent;border-right:7px solid var(--content)}
  .avatar{position:absolute;left:12px;top:535px;width:36px;height:36px;border-radius:50%;background:linear-gradient(#8a6a55,#c9a48b);border:2px solid #e8f0ff}
  .page-title{position:absolute;left:85px;top:84px;font-size:12.5px;font-weight:600}
  .legend{position:absolute;right:26px;top:86px;display:flex;gap:30px;font-size:10px;color:var(--muted);align-items:center}
  .legend span{display:flex;align-items:center;gap:8px}
  .warn{width:12px;height:11px}
  .info-dot{width:12px;height:12px;border-radius:50%;background:var(--amber);color:#fff;font-size:8px;display:inline-flex;align-items:center;justify-content:center;font-weight:700}
  .card{position:absolute;top:127px;width:274px;height:223px;background:var(--card);box-shadow:0 1px 3px rgba(0,0,0,.12);text-align:center}
  .card-head{height:37px;background:var(--black);color:#fff;font-size:13.5px;font-weight:600;display:flex;align-items:center;justify-content:center;gap:9px}
  .i-badge{width:14px;height:14px;border-radius:50%;background:#fff;color:#000;font-size:10px;font-weight:700;display:inline-flex;align-items:center;justify-content:center}
  .amount{margin-top:25px;font-size:26px;color:#555;font-weight:400}
  .detail{position:absolute;left:0;right:0;top:137px;font-size:13px;color:#555;line-height:18px}
  .detail.stack{top:120px}
  .btns{position:absolute;left:0;right:0;top:175px;display:flex;justify-content:center;gap:7px}
  .btn{width:113px;height:34px;background:var(--btn);color:#fff;font-size:12.5px;font-weight:600;display:flex;align-items:center;justify-content:center}
  .panel{position:absolute;top:375px;height:252px;background:var(--card);box-shadow:0 1px 3px rgba(0,0,0,.12)}
  .panel-head{height:40px;background:#ececec;font-size:13.5px;display:flex;align-items:center;justify-content:center;gap:8px}
  .panel-head svg{width:16px;height:16px}
  table{border-collapse:collapse;width:100%;table-layout:fixed}
  th{height:29px;font-size:12.5px;font-weight:400;color:#444;border:1px solid var(--line);border-top:none}
  td{height:45.5px;font-size:11px;color:#666;text-align:center;border:1px solid var(--line);line-height:15px}
  tr>*:first-child{border-left:none}
  tr>*:last-child{border-right:none}
  .active{color:var(--green)}
  .pending{color:var(--red)}
</style>
</head>
<body>
<div class="app">
  <header class="topbar">
    <div class="brand"><span class="brand-dot"></span>LedgerHarbor</div>
    <nav class="nav">
      <div class="nav-item"><svg viewBox="0 0 12 12"><path d="M6 1 1 6h1.5v5h3V8h1v3h3V6H11z"/></svg>Home</div>
      <div class="nav-item"><svg viewBox="0 0 12 12"><circle cx="7" cy="2" r="1.4"/><path d="M5 4h3l-1 3 2 4H7.5L6 8 4.5 11H3l2-5-2 1V5z"/></svg>Job Center</div>
      <div class="nav-item"><svg viewBox="0 0 12 12"><path d="M0 2h12v8H0zM1 4h10V3H1zm0 2v3h10V6z"/></svg>Payments</div>
      <div class="nav-item"><svg viewBox="0 0 12 12"><path d="M6 0 0 3v1h12V3zM1 5h2v5H1zm4 0h2v5H5zm4 0h2v5H9zM0 11h12v1H0z"/></svg>Credit Management</div>
      <div class="nav-item"><svg viewBox="0 0 12 12"><path d="M3 1h7v10H2V2zm1 2v1h5V3zm0 2v1h5V5zm0 2v1h4V7z"/></svg>Prelien Center</div>
    </nav>
    <div class="tools">
      <svg viewBox="0 0 16 16"><rect x="1" y="3" width="14" height="10"/><path d="m1 3 7 6 7-6"/></svg>
      <svg viewBox="0 0 16 16"><path d="M3 1h3l1 4-2 1a8 8 0 0 0 5 5l1-2 4 1v3c0 1-1 2-2 2A13 13 0 0 1 1 3c0-1 1-2 2-2z" fill="#fff" stroke="none"/></svg>
      <svg viewBox="0 0 16 16"><circle cx="8" cy="8" r="6.5"/><path d="M5 7a3 3 0 0 1 6 0M11 9a3 3 0 0 1-6 0"/></svg>
      <svg viewBox="0 0 16 16"><path d="M9 2H2v12h7M6 8h9M12 5l3 3-3 3"/></svg>
    </div>
  </header>

  <aside class="sidebar">
    <span class="side-pointer"></span>
    <svg class="side-icon" style="top:25px" viewBox="0 0 16 16"><circle cx="8" cy="8" r="6.5"/><path d="m10.5 5.5-2 3.5-3 1.5 2-3.5z"/></svg>
    <svg class="side-icon" style="top:64px" viewBox="0 0 16 16"><circle cx="8" cy="5" r="3.2"/><path d="M2 15c0-4 3-5.5 6-5.5s6 1.5 6 5.5z"/></svg>
    <svg class="side-icon" style="top:103px" viewBox="0 0 16 16"><path d="M3 13 11 5l2 2-8 8H3zM10 3l3 3"/></svg>
    <svg class="side-icon" style="top:143px" viewBox="0 0 16 16"><rect x="2" y="3" width="12" height="11"/><path d="M2 6h12M5 1v3M11 1v3M5 9h1M8 9h1M11 9h1M5 12h1M8 12h1"/></svg>
    <svg class="side-icon" style="top:182px" viewBox="0 0 16 16"><path d="M3 1h7l3 3v11H3z"/></svg>
    <svg class="side-icon" style="top:222px" viewBox="0 0 16 16"><rect x="1" y="4" width="11" height="7" rx="1"/><path d="M4 2h11v7M4 11v3l3-3"/></svg>
    <svg class="side-icon" style="top:261px" viewBox="0 0 16 16"><path d="M2 4h12M6 4V2h4v2M4 4l1 11h6l1-11M7 7v5M9 7v5"/></svg>
    <div class="avatar" role="img" aria-label="User profile photo"></div>
  </aside>

  <h1 class="page-title">Dashboard</h1>
  <div class="legend">
    <span><svg class="warn" viewBox="0 0 12 11"><path d="M6 0 12 11H0z" fill="#2bb24c"/><path d="M6 4v3.5M6 8.6v1" stroke="#fff" stroke-width="1.3"/></svg>Indicates an Action is Required</span>
    <span><i class="info-dot">?</i>Information only-no action required</span>
  </div>

  <section class="card" style="left:87px">
    <div class="card-head"><i class="i-badge">i</i>Available Master Credit</div>
    <div class="amount">$129,500.00</div>
    <p class="detail">Master Credit Limit: $250,000.00</p>
    <div class="btns"><span class="btn">Setup New Job</span></div>
  </section>
  <section class="card" style="left:395px">
    <div class="card-head"><i class="i-badge">i</i>Last Payment</div>
    <div class="amount">$500.00</div>
    <p class="detail">Last Payment date: 6/28/2016</p>
    <div class="btns"><span class="btn">View Payments</span><span class="btn">View Billings</span></div>
  </section>
  <section class="card" style="left:703px">
    <div class="card-head"><svg width="16" height="14" viewBox="0 0 12 11"><path d="M6 0 12 11H0z" fill="#2bb24c"/><path d="M6 4v3.5M6 8.6v1" stroke="#000" stroke-width="1.3"/></svg>Next Payment</div>
    <div class="amount">$158.95</div>
    <p class="detail stack">Due Date: 7/11/2016<br>Current Principal: $9,968.46<br>Minimum Interest/Fees: $158.9</p>
    <div class="btns"><span class="btn">Make Payment</span></div>
  </section>

  <section class="panel" style="left:85px;width:432px">
    <div class="panel-head"><svg viewBox="0 0 16 16"><path d="M1 15h14M2 14V8M5 14V4M8 14V7M11 14V5M14 14V9" stroke="#111" stroke-width="1.8"/></svg>Task Summery</div>
    <table>
      <colgroup><col style="width:36px"><col style="width:106px"><col style="width:212px"><col style="width:78px"></colgroup>
      <tr><th></th><th>Task</th><th>Status</th><th>Received</th></tr>
      <tr><td><i class="info-dot">?</i></td><td>Supplier Invoice</td><td>Confirmation by Account Manager<br><span class="pending">Pending</span></td><td>5/1/2016</td></tr>
      <tr><td></td><td></td><td></td><td></td></tr>
      <tr><td></td><td></td><td></td><td></td></tr>
      <tr><td></td><td></td><td></td><td></td></tr>
    </table>
  </section>

  <section class="panel" style="left:530px;width:447px">
    <div class="panel-head"><svg viewBox="0 0 16 16"><path d="M2 14 10 6M6 2l8 8M10 2l4 4-2 2-4-4zM2 11l3 3" stroke="#111" stroke-width="2"/></svg>Active Jobs</div>
    <table>
      <tr><th>Job#</th><th>Job Name</th><th>Status</th><th>Credit Limit</th><th>Avail. Credit</th></tr>
      <tr><td>pc101-001</td><td>Job #001</td><td class="active">Active</td><td>$50,100.00</td><td>$35,100.00</td></tr>
      <tr><td>pc101-002</td><td>Job #002</td><td class="active">Active</td><td>$40,000.00</td><td>$2,000.00</td></tr>
      <tr><td>pc101-003</td><td>Job #003</td><td class="active">Active</td><td>$22,000.00</td><td>$0.00</td></tr>
      <tr><td>pc101-004</td><td>Job #004</td><td class="active">Active</td><td>$10,400.00</td><td>$10,400.00</td></tr>
    </table>
  </section>
</div>
</body>
</html>
```